Safety Company in need of a Tri-fold Brochure design

We need a tri-fold brochure for our technicians to hand out to clients. We need to show the services we provide. Design, engineering, fabrication, installation, testing, Operating/Work procedures, training, certification of Fall Protection/Window Cleaning Equipment.

Target Market(s)

building owners, property managers

Industry/Entity Type

It Company

Font styles to use
Sans Serif
Script

Colors
0455a3
ec1f27
ffffff

Requirements
Must have
• mission statement, 24 hour response policy, photos of services

```html
<!DOCTYPE html>
<html lang="en">
<head>
<meta charset="utf-8">
<title>Exterior Building Access – Services Brochure</title>
<link rel="stylesheet" href="https://fonts.googleapis.com/css2?family=Oswald:wght@500;700&family=Open+Sans:wght@600&family=Arimo:wght@600&display=swap">
<style>
  :root {
    --brand-blue: #3a78bd;
    --brand-red: #ec1f27;
    --ink: #141414;
    --ink-soft: #333333;
    --paper: #f2f2f2;
    --white: #ffffff;
  }
  * { margin: 0; padding: 0; box-sizing: border-box; }
  html, body { width: 1200px; height: 849px; overflow: hidden; background: var(--white); }
  .brochure {
    position: relative; width: 1200px; height: 849px; overflow: hidden;
    background: linear-gradient(180deg, #f4f4f4 0%, #e6e6e6 45%, #efefef 70%, #f7f7f7 100%);
    font-family: "Arimo", Arial, sans-serif;
  }
  .artwork { position: absolute; inset: 0; }
  .mission-icon { position: absolute; left: 14px; top: 14px; width: 90px; height: 90px; }
  .mission-title {
    position: absolute; left: 104px; top: 38px;
    font-family: "Oswald", "Arial Narrow", sans-serif; font-weight: 700;
    font-size: 50px; line-height: 1; color: #1c1c1c; letter-spacing: 0.5px;
  }
  .mission-statement, .commitment {
    position: absolute; text-align: center;
    font-family: "Oswald", "Arial Narrow", sans-serif; font-weight: 500;
    color: var(--ink-soft); font-size: 17px; line-height: 28.8px;
  }
  .mission-statement { left: 34px; top: 123px; width: 300px; }
  .commitment { left: 395px; top: 20px; width: 400px; }
  .section-tab {
    position: absolute; height: 42px; padding-left: 12px;
    background: var(--brand-blue); color: var(--white);
    border-radius: 0 21px 21px 0;
    font-family: "Open Sans", Arial, sans-serif; font-weight: 600;
    font-size: 21px; line-height: 42px; white-space: nowrap;
  }
  .section-tab.is-long { font-size: 19px; }
  .section-body {
    position: absolute; color: var(--ink);
    font-size: 12.2px; line-height: 17.6px; font-weight: 600;
  }
  .section-body p + p { margin-top: 17.6px; }
</style>
</head>
<body>
<main class="brochure">
  <svg class="artwork" width="1200" height="849" viewBox="0 0 1200 849">
    <defs>
      <linearGradient id="photoTones" x1="0" y1="0" x2="1" y2="0">
        <stop offset="0" stop-color="#c9cacb"/>
        <stop offset="0.35" stop-color="#b9b4ae"/>
        <stop offset="0.6" stop-color="#a8b4bf"/>
        <stop offset="0.8" stop-color="#8aa8c8"/>
        <stop offset="1" stop-color="#6f7f8f"/>
      </linearGradient>
      <linearGradient id="photoFade" x1="0" y1="0" x2="0" y2="1">
        <stop offset="0.7" stop-color="#ffffff" stop-opacity="0"/>
        <stop offset="1" stop-color="#efefef" stop-opacity="0.9"/>
      </linearGradient>
    </defs>
    <g role="img" aria-label="Photos of services: wall anchor, davit system, engineering drawing, roof tripod anchor, guarded skylight and a suspended work platform on a high-rise">
      <path d="M0,232 C300,240 650,222 860,150 L1050,60 L1200,0 L1200,530 C1000,480 720,405 0,390 Z" fill="url(#photoTones)"/>
      <path d="M0,232 C300,240 650,222 860,150 L1050,60 L1200,0 L1200,530 C1000,480 720,405 0,390 Z" fill="url(#photoFade)"/>
    </g>
    <circle cx="459" cy="279" r="45" fill="#8a5a3c" stroke="#ffffff" stroke-width="2" role="img" aria-label="Photo inset of a rooftop seating area"/>
    <path d="M0,226 C350,238 700,214 1200,-6 L1200,36 C700,248 350,242 0,236 Z" fill="var(--brand-red)"/>
    <path d="M0,372 C300,368 600,386 820,432 L820,441 C600,396 300,380 0,384 Z" fill="var(--brand-red)"/>
    <g class="response-badge">
      <ellipse cx="900" cy="118" rx="92" ry="40" fill="#b9b9b9" opacity="0.85"/>
      <circle cx="884" cy="88" r="64" fill="var(--brand-blue)"/>
      <circle cx="882" cy="86" r="61" fill="var(--brand-red)"/>
      <circle cx="882" cy="86" r="53" fill="#e9e9e9"/>
      <circle cx="882" cy="86" r="48" fill="#f8f8f8"/>
      <text x="882" y="82" text-anchor="middle" font-family="Oswald, sans-serif" font-weight="700" font-size="27" fill="var(--brand-red)">24 HRS</text>
      <text x="882" y="104" text-anchor="middle" font-family="Oswald, sans-serif" font-weight="700" font-size="21" fill="var(--brand-red)">RESPONSE</text>
    </g>
  </svg>

  <svg class="mission-icon" viewBox="0 0 90 90" role="img" aria-label="Target icon">
    <circle cx="42" cy="50" r="34" fill="#d8d8d8"/>
    <circle cx="42" cy="50" r="26" fill="var(--brand-red)"/>
    <circle cx="42" cy="50" r="18" fill="#ffffff"/>
    <circle cx="42" cy="50" r="10" fill="var(--brand-red)"/>
  </svg>
  <h1 class="mission-title">OUR MISSION</h1>
  <p class="mission-statement">to provide a cost effective, safe,<br>and compliant system for accessing the<br>exterior of buildings</p>
  <p class="commitment">We are committed to&nbsp; creating long lasting relationships<br>built on positive, responsive quality service and<br>reinforced using strong internal teamwork.<br>We are committed to our clientele to complete all<br>projects, regardless of complete all projects, regardless<br>of adversity faced</p>

  <h2 class="section-tab" style="left:0;top:419px;width:318px;">DESIGN&nbsp;&nbsp; AND&nbsp;&nbsp; ENGINEERING</h2>
  <div class="section-body" style="left:10px;top:466px;width:384px;">
    <p>We have the industry experience and expertise&nbsp; to design and engineer state of the art complete exterior building maintenance systems that meet your&nbsp; specific needs while ensuring safety and compliance. These include Powered Platforms, Stabilization Systems, Davit Systems and Outrigger Systems</p>
  </div>

  <h2 class="section-tab" style="left:0;top:576px;width:318px;">INSTALLATION</h2>
  <div class="section-body" style="left:10px;top:622px;width:388px;">
    <p>We will design, fabricate, and install your&nbsp; complete exterior building maintenance system, including: stabilization systems, outrigger systems, and davit systems as well as all safety equipment necessary to meet OSHA regulations&nbsp; and keep workers safe.</p>
  </div>

  <h2 class="section-tab" style="left:0;top:710px;width:320px;">Powered&nbsp;&nbsp; Platforms</h2>
  <div class="section-body" style="left:12px;top:756px;width:380px;">
    <p>Powered, suspended work platforms are custom order items, modular by nature and designed to match your building’s needs. We provide this equipment with versatility built-in and safety always in mind</p>
  </div>

  <h2 class="section-tab" style="left:402px;top:438px;width:317px;">FALL&nbsp;&nbsp; PROTECTION</h2>
  <div class="section-body" style="left:410px;top:492px;width:390px;">
    <p>We are specialist in safety Anchors &amp; Lifelines&nbsp; these can be used for the tie-back of Controlled descent equipment (CDA or CDE) and must be designed to support up to a 5,000 lb. load.</p>
    <p>Roofs must have a 42” high parapet or guardrail for passive fall protection of any persons on the roof. Other areas which require guardrails is around skylights, floor openings, roof hatches and other sunken areas on the roof, to prevents falls that can result in serious injury or even death</p>
  </div>

  <h2 class="section-tab is-long" style="left:398px;top:663px;width:400px;">Testing,Certification&nbsp;&nbsp; and&nbsp;&nbsp; Inspection</h2>
  <div class="section-body" style="left:406px;top:715px;width:396px;">
    <p>We test all of your equipment and make sure you have the certifications required to meet all relevant OSHA, State, and Federal safety standards. All suspended maintenance equipment, components and safety anchors or horizontal lifelines, must be inspected annually, as a minimum requirement. A similar inspection should be performed following any major alteration.</p>
  </div>

  <h2 class="section-tab" style="left:798px;top:523px;width:158px;">TRAINING</h2>
  <div class="section-body" style="left:808px;top:574px;width:388px;">
    <p>We are actively involved in multiple associations providing safety training courses and demonstrations. In addition, we offer a Competent Person Training Program to meet standards set forth by OSHA. Our program will provide workers with an in-depth knowledge of safety procedures in the use of exterior building maintenance equipment, the many facets of safety involved with the operation of the equipment and protecting themselves during an emergency.</p>
    <p>For Window Cleaning Companies Completion of the course can be used to provide your insurance company with proof of ongoing safety training and can also help you to demonstrate to clients that you are complying with CA OSHA / Fed OSHA safety codes.</p>
  </div>
</main>
</body>
</html>
```